Business card for massage therapy company called Brook Fern Wellness

Need business card for massage therapy company called Brook Fern Wellness. Would like my logo on the front and the back of the card I have 3 options of logos and you can play with what looks better.

Would like this information displayed on the back of the card:

Marcus Ellery
Licensed Massage Therapist
321-555-0147
brookfern-example.com
brookfern_rest_

```html
<!DOCTYPE html>
<html lang="en">
<head>
<meta charset="utf-8">
<title>Brook Fern Wellness — Business Card</title>
<link href="https://fonts.googleapis.com/css2?family=Poppins:wght@400;500;700&display=swap" rel="stylesheet">
<style>
  :root {
    --backdrop: #2b2c2f;
    --sage: #727860;
    --sage-deep: #5f664e;
    --sage-faint: #858b72;
    --clay: #c68b62;
    --paper: #ffffff;
    --ink-soft: #6d6d6d;
    --rule: #e3e3e3;
  }
  * { box-sizing: border-box; margin: 0; padding: 0; }
  html, body {
    width: 1200px;
    height: 952px;
    overflow: hidden;
    background: var(--backdrop);
    font-family: "Poppins", sans-serif;
  }
  .card-set {
    position: relative;
    width: 1200px;
    height: 952px;
  }
  .card {
    position: absolute;
    top: 326px;
    width: 520px;
    height: 300px;
    border-radius: 3px;
    overflow: hidden;
  }
  /* Front */
  .card--front {
    left: 60px;
    background: var(--sage);
  }
  .front-accent {
    position: absolute;
    left: 40px;
    top: -60px;
    width: 230px;
    height: 230px;
    border: 2px solid var(--sage-faint);
    border-radius: 50%;
  }
  .front-brand {
    position: absolute;
    left: 240px;
    top: 160px;
    color: var(--paper);
    font-weight: 400;
    font-size: 30px;
    line-height: 1.1;
  }
  /* Back */
  .card--back {
    left: 620px;
    background: var(--paper);
    display: flex;
    align-items: center;
  }
  .back-brand {
    width: 250px;
    padding-left: 38px;
    color: var(--sage);
    font-weight: 400;
    font-size: 27px;
    line-height: 1.1;
  }
  .back-divider {
    width: 1px;
    height: 170px;
    background: var(--rule);
  }
  .back-details {
    padding-left: 26px;
  }
  .holder-name {
    color: var(--sage-deep);
    font-weight: 700;
    font-size: 22px;
    letter-spacing: 0.5px;
    text-transform: uppercase;
  }
  .holder-role {
    color: var(--ink-soft);
    font-size: 11.5px;
    margin-bottom: 16px;
  }
  .contact-list { list-style: none; }
  .contact-item {
    display: flex;
    align-items: center;
    gap: 8px;
    color: var(--ink-soft);
    font-size: 12.5px;
    margin-bottom: 6px;
  }
  .contact-icon { width: 12px; height: 12px; flex: none; }
</style>
</head>
<body>
  <main class="card-set">
    <section class="card card--front" aria-label="Card front">
      <div class="front-accent"></div>
      <p class="front-brand">Brook Fern<br>Wellness</p>
    </section>

    <section class="card card--back" aria-label="Card back">
      <p class="back-brand">Brook Fern<br>Wellness</p>
      <div class="back-divider"></div>
      <div class="back-details">
        <h1 class="holder-name">Marcus Ellery</h1>
        <p class="holder-role">Licensed Massage Therapist</p>
        <ul class="contact-list">
          <li class="contact-item">
            <svg class="contact-icon" viewBox="0 0 24 24" aria-hidden="true"><path fill="#c68b62" d="M6.6 10.8a15.1 15.1 0 0 0 6.6 6.6l2.2-2.2a1 1 0 0 1 1-.25 11.4 11.4 0 0 0 3.6.57 1 1 0 0 1 1 1V20a1 1 0 0 1-1 1A17 17 0 0 1 3 4a1 1 0 0 1 1-1h3.5a1 1 0 0 1 1 1c0 1.25.2 2.45.57 3.57a1 1 0 0 1-.25 1z"/></svg>
            321-555-0147
          </li>
          <li class="contact-item">
            <svg class="contact-icon" viewBox="0 0 24 24" aria-hidden="true"><rect x="2" y="5" width="20" height="14" rx="1.5" fill="#c68b62"/><path d="M3 6l9 7 9-7" fill="none" stroke="#fff" stroke-width="1.6"/></svg>
            brookfern-example.com
          </li>
          <li class="contact-item">
            <svg class="contact-icon" viewBox="0 0 24 24" aria-hidden="true"><circle cx="12" cy="12" r="9.5" fill="none" stroke="#c68b62" stroke-width="2.4"/><circle cx="12" cy="12" r="3.5" fill="#c68b62"/></svg>
            brookfern_rest_
          </li>
        </ul>
      </div>
    </section>
  </main>
</body>
</html>
```